Online training business needs new website

We need a new wordpress website as a result of a rebranding. The business is a crisis management training company focussed on online training and simulation exercises. We only need a 4 page site - home, about us, contact us and blog. However we must be able to add additional tabs in the header to redirect to our sales and marketing system (Velmora). As these change from time to time, we must be able to add and delete as required.The site must be editable by us, with a basic understanding of wordpress and no understanding of coding. We don't want to have to employ someone to change text, add posts or add a new workshops etc. The theme chosen must be easy to edit by a beginner.

Target Market(s)

Senior managers food and consumer goods companies

Industry/Entity Type

Consulting

Coding

Coded - Design and coding required

Font styles to use
Sans Serif

Requirements
Must have
• Home page, about us, contact us, blog
• Colour scheme from logo (attached) - maroon, blue and grey
• If you go to the current website "brightharbourgroup.com" and click on the "workshops" tab you will see the content I need on the home page for the stormpilotlabs.com site
Nice to have
• Modern, simple and minimalist design is preferred

```html
<!DOCTYPE html>
<html lang="en">
<head>
<meta charset="utf-8">
<title>Storm Pilot – Crisis Workshops &amp; Simulations</title>
<link href="https://fonts.googleapis.com/css2?family=Roboto:wght@400;500;700&family=Open+Sans:wght@400;600&display=swap" rel="stylesheet">
<style>
:root{
  --maroon:#7d0c3f;
  --navy:#0d3b6e;
  --blue:#134f86;
  --grey:#5a5a5a;
  --ice:#e5eff9;
  --line:#dcdcdc;
  --white:#ffffff;
}
*{box-sizing:border-box;margin:0;padding:0}
html,body{width:1200px;height:2826px;overflow:hidden;background:var(--white)}
body{font-family:"Roboto",Arial,sans-serif;color:var(--navy)}
.page{position:relative;width:1200px;height:2826px;overflow:hidden}
.abs{position:absolute}

/* header */
.site-header{position:absolute;left:0;top:0;width:1200px;height:108px;background:var(--white);z-index:5}
.brand{position:absolute;left:165px;top:6px;width:140px;height:140px;border-radius:50%;background:var(--white);display:flex;align-items:center;justify-content:center}
.brand-name{font:700 27px/1 "Roboto",sans-serif;color:var(--maroon);text-align:center;letter-spacing:1px}
.main-nav{position:absolute;top:48px;left:537px;display:flex;gap:0}
.main-nav a{font:400 17px/1 "Roboto",sans-serif;color:var(--navy);text-decoration:none;margin-right:46px}
.main-nav a.is-active{color:var(--maroon)}

/* hero */
.hero{position:absolute;left:0;top:108px;width:1200px;height:640px}
.hero-photo{position:absolute;inset:0;background:linear-gradient(120deg,#6b6a6c 0%,#a7a5a3 35%,#cfcdca 55%,#8e8c8c 80%,#5e5d60 100%)}
.hero-shade{position:absolute;inset:0;background:rgba(40,40,48,.35)}
.hero-brand{position:absolute;top:75px;width:100%;text-align:center;font:700 34px/1 "Roboto",sans-serif;color:#3b3b3d;letter-spacing:1px}
.hero-title{position:absolute;top:172px;width:100%;text-align:center;font:700 38px/47px "Roboto",sans-serif;color:var(--white);text-transform:uppercase}
.btn{display:inline-block;background:var(--maroon);color:var(--white);font:400 17px/52px "Roboto",sans-serif;text-transform:uppercase;text-align:center;border-radius:26px}
.hero .btn{position:absolute;left:512px;top:331px;width:175px}
.hero-curve{position:absolute;left:0;top:600px;width:1200px;height:150px}

/* about */
.about-title{position:absolute;top:748px;width:100%;text-align:center;font:400 35px/1 "Roboto",sans-serif;color:var(--navy)}
.about-title span{color:var(--maroon)}
.about-intro{position:absolute;top:808px;left:230px;width:740px;text-align:center;font:400 18px/31px "Open Sans",sans-serif;color:var(--grey)}
.fact{position:absolute;width:428px;height:168px;background:var(--white);box-shadow:0 0 6px rgba(0,0,0,.16);display:flex;align-items:center}
.fact-icon{position:absolute;left:22px;top:38px;width:92px;height:92px}
.fact p{position:absolute;left:124px;right:20px;font:400 18px/26px "Roboto",sans-serif;color:var(--navy)}

/* blogs */
.blogs-band{position:absolute;left:0;top:1380px;width:1200px;height:720px}
.blogs-title{position:absolute;top:1480px;width:100%;text-align:center;font:400 36px/1 "Roboto",sans-serif;color:var(--white)}
.blogs-mark{position:absolute;left:586px;top:1434px;width:28px;height:28px;border:3px solid var(--white);border-radius:50%}
.post{position:absolute;background:var(--white)}
.post-media{position:absolute}
.post-date{font:700 12px/1 "Roboto",sans-serif;color:var(--maroon);text-transform:uppercase;display:flex;align-items:center;gap:6px}
.post-title{font:400 18px/1.2 "Roboto",sans-serif;color:var(--navy);margin-top:12px}
.post-excerpt{font:400 13px/17px "Open Sans",sans-serif;color:var(--grey);margin-top:10px}
.post-more{font:400 13px/1 "Roboto",sans-serif;color:var(--blue);text-transform:uppercase;margin-top:16px;display:block}
.post-body{position:absolute}

/* contact */
.contact-zone{position:absolute;left:0;top:2060px;width:1200px;height:615px;background:var(--ice)}
.contact-form{position:absolute;left:170px;top:2170px;width:444px;height:393px;background:var(--maroon);padding:0 38px}
.field{position:absolute;left:38px;right:38px;border-bottom:1px solid rgba(255,255,255,.7);font:400 15px/1 "Roboto",sans-serif;color:var(--white);text-transform:uppercase;padding-bottom:12px}
.submit{position:absolute;left:38px;top:310px;width:176px;height:44px;background:var(--navy);color:var(--white);font:500 18px/44px "Roboto",sans-serif;text-align:center;text-transform:uppercase}
.contact-info{position:absolute;left:682px;top:2172px;width:420px}
.contact-info h2{font:400 31px/1 "Roboto",sans-serif;color:var(--navy);text-transform:uppercase}
.info-label{font:500 15px/1 "Roboto",sans-serif;color:#333;text-transform:uppercase;margin-top:32px}
.info-value{font:400 17px/25px "Roboto",sans-serif;color:#333;text-transform:uppercase;margin-top:6px}
.social{display:flex;gap:28px;margin-top:18px;padding-left:8px}
.social span{width:24px;height:24px;border-radius:50%;background:var(--maroon);display:block}

/* footer */
.site-footer{position:absolute;left:0;top:2675px;width:1200px;height:151px;background:var(--white)}
.footer-nav{position:absolute;top:42px;width:100%;text-align:center}
.footer-nav a{font:400 18px/1 "Roboto",sans-serif;color:var(--navy);text-decoration:none;margin:0 19px;text-transform:uppercase}
.copyright{position:absolute;top:84px;width:100%;text-align:center;font:400 15px/1 "Roboto",sans-serif;color:#444}
</style>
</head>
<body>
<div class="page">

  <header class="site-header">
    <div class="brand"><span class="brand-name">STORM<br>PILOT</span></div>
    <nav class="main-nav">
      <a href="#" class="is-active">HOME</a>
      <a href="#">ABOUT US</a>
      <a href="#">CONTACT US</a>
      <a href="#">BLOG</a>
    </nav>
  </header>

  <section class="hero">
    <div class="hero-photo" role="img" aria-label="Photo of business people meeting around a table with laptops"></div>
    <div class="hero-shade"></div>
    <div class="hero-brand">STORM PILOT</div>
    <h1 class="hero-title">Workshops &amp; simulations to<br>help food and consumer goods<br>companies prevent a crisis</h1>
    <a class="btn" href="#">Read more</a>
  </section>
  <svg class="hero-curve" viewBox="0 0 1200 150" aria-hidden="true">
    <path d="M0 140 Q600 40 1200 140 L1200 150 L0 150 Z" fill="#ffffff"/>
    <path d="M110 125 Q600 50 1090 125" fill="none" stroke="#0d3b6e" stroke-width="5"/>
    <path d="M160 122 Q600 62 1040 122" fill="none" stroke="#7d0c3f" stroke-width="2"/>
    <circle cx="600" cy="72" r="34" fill="#ffffff"/>
    <circle cx="600" cy="72" r="22" fill="none" stroke="#0d3b6e" stroke-width="4"/>
  </svg>

  <section>
    <h2 class="about-title"><span>ABOUT</span> STORM PILOT</h2>
    <p class="about-intro">If you are a food or consumer goods manufacturer, distributor or retailer, a major incident or a product recall can quickly escalate into a crisis!</p>

    <div class="fact" style="left:160px;top:935px">
      <svg class="fact-icon" viewBox="0 0 92 92" aria-hidden="true">
        <circle cx="40" cy="50" r="34" fill="#c7d6e6" opacity=".6"/>
        <path d="M40 20 l-6 -8 h24 l-6 8 Z M34 22 h18 M30 30 Q20 48 26 60 h34 Q66 48 56 30 Z" fill="#fff" stroke="#7d0c3f" stroke-width="2.5" stroke-linejoin="round"/>
        <text x="43" y="53" font-family="Roboto,sans-serif" font-size="18" fill="#7d0c3f" text-anchor="middle">$</text>
      </svg>
      <p>The average cost of a crisis is $10m and 25% cost over $100m</p>
    </div>
    <div class="fact" style="left:606px;top:935px">
      <svg class="fact-icon" viewBox="0 0 92 92" aria-hidden="true">
        <circle cx="40" cy="50" r="34" fill="#c7d6e6" opacity=".6"/>
        <polyline points="22,22 36,32 48,30 60,46 74,44" fill="none" stroke="#7d0c3f" stroke-width="2.5"/>
        <g fill="#7d0c3f"><circle cx="22" cy="22" r="4"/><circle cx="36" cy="32" r="4"/><circle cx="48" cy="30" r="4"/><circle cx="60" cy="46" r="4"/></g>
        <path d="M70 40 l6 4 -7 3" fill="none" stroke="#7d0c3f" stroke-width="2.5"/>
      </svg>
      <p>Small and medium size businesses often don't survive at all</p>
    </div>
    <div class="fact" style="left:160px;top:1121px">
      <svg class="fact-icon" viewBox="0 0 92 92" aria-hidden="true">
        <circle cx="40" cy="50" r="34" fill="#c7d6e6" opacity=".6"/>
        <rect x="34" y="22" width="32" height="32" rx="6" fill="#fff" stroke="#7d0c3f" stroke-width="2.5"/>
        <path d="M43 31 l14 14 M57 31 l-14 14" stroke="#7d0c3f" stroke-width="2.5"/>
      </svg>
      <p>The largest cost to any size business is to your reputation &amp; brand - that impacts customer relationships &amp; long term sales!</p>
    </div>
    <div class="fact" style="left:606px;top:1121px">
      <svg class="fact-icon" viewBox="0 0 92 92" aria-hidden="true">
        <circle cx="40" cy="50" r="34" fill="#c7d6e6" opacity=".6"/>
        <path d="M50 14 L74 56 H26 Z" fill="#fff" stroke="#7d0c3f" stroke-width="2.5" stroke-linejoin="round"/>
        <path d="M50 28 v16" stroke="#7d0c3f" stroke-width="3"/>
        <circle cx="50" cy="50" r="2" fill="#7d0c3f"/>
      </svg>
      <p>Reputation risk remains the number one concern of senior executives, but most are unprepared for a crisis</p>
    </div>
  </section>

  <div class="contact-zone"></div>

  <svg class="blogs-band" viewBox="0 0 1200 720" aria-hidden="true">
    <path d="M0 40 Q560 -20 1200 80 L1200 660 Q640 780 0 640 Z" fill="#7d0c3f"/>
    <path d="M0 60 Q560 10 1200 100 L1200 630 Q640 760 0 615 Z" fill="#134f86"/>
    <path d="M0 60 Q560 10 1200 100 L1200 630 Q640 760 0 615 Z" fill="#0d3b6e" opacity=".35"/>
  </svg>
  <div class="blogs-mark"></div>
  <h2 class="blogs-title">OUR BLOGS</h2>

  <article class="post" style="left:148px;top:1561px;width:435px;height:384px">
    <div class="post-media" role="img" aria-label="Photo of a hand stopping falling wooden dominoes" style="left:0;top:0;width:435px;height:209px;background:linear-gradient(160deg,#3a3430,#7a5a3a 60%,#2a2522)"></div>
    <div class="post-body" style="left:26px;top:232px;right:24px">
      <div class="post-date"><svg width="13" height="13" viewBox="0 0 13 13"><rect x="1" y="2" width="11" height="10" fill="none" stroke="#7d0c3f" stroke-width="1.6"/><path d="M1 5h11" stroke="#7d0c3f" stroke-width="1.6"/></svg>30 Dec 2018</div>
      <div class="post-title">Pellentesque faucibus Ut accumsan ultricies</div>
      <p class="post-excerpt">Pellentesque faucibus Ut accumsan ultricies elit Maecenas at justo id velit placerat molestie Donec dictum lectus non</p>
      <span class="post-more">Read more</span>
    </div>
  </article>

  <article class="post" style="left:599px;top:1561px;width:444px;height:186px">
    <div class="post-media" role="img" aria-label="Photo of a team reviewing charts on a desk" style="left:0;top:0;width:216px;height:186px;background:linear-gradient(135deg,#8a7a5e,#b7b3a6 50%,#5d6a70)"></div>
    <div class="post-body" style="left:240px;top:22px;right:14px">
      <div class="post-date"><svg width="13" height="13" viewBox="0 0 13 13"><rect x="1" y="2" width="11" height="10" fill="none" stroke="#7d0c3f" stroke-width="1.6"/><path d="M1 5h11" stroke="#7d0c3f" stroke-width="1.6"/></svg>21 Dec 2018</div>
      <div class="post-title">Blog Title here</div>
      <p class="post-excerpt">Pellentesque faucibus Ut accumsan ultricies elit Maecenas at justo id velit placerat</p>
      <span class="post-more" style="margin-top:10px">Read more</span>
    </div>
  </article>

  <article class="post" style="left:599px;top:1758px;width:444px;height:187px">
    <div class="post-media" role="img" aria-label="Photo of colleagues at a meeting table" style="left:0;top:0;width:216px;height:187px;background:linear-gradient(135deg,#d9d6d0,#9f8e78 55%,#4b4a4c)"></div>
    <div class="post-body" style="left:240px;top:22px;right:14px">
      <div class="post-date"><svg width="13" height="13" viewBox="0 0 13 13"><rect x="1" y="2" width="11" height="10" fill="none" stroke="#7d0c3f" stroke-width="1.6"/><path d="M1 5h11" stroke="#7d0c3f" stroke-width="1.6"/></svg>14 Dec 2018</div>
      <div class="post-title">Blog Title here</div>
      <p class="post-excerpt">Pellentesque faucibus Ut accumsan ultricies elit Maecenas at justo id velit placerat</p>
      <span class="post-more" style="margin-top:10px">Read more</span>
    </div>
  </article>

  <form class="contact-form">
    <div class="field" style="top:40px">Name</div>
    <div class="field" style="top:93px">Email</div>
    <div class="field" style="top:146px">Phone Number</div>
    <div class="field" style="top:199px;height:86px">Message</div>
    <div class="submit">Submit</div>
  </form>

  <div class="contact-info">
    <h2>Contact Us</h2>
    <div class="info-label">Address</div>
    <div class="info-value">14 Harbour Lane, Eastfield WA 6099<br>Perth – Australia</div>
    <div class="info-label">Phone Number</div>
    <div class="info-value">0400 555 123</div>
    <div class="info-label">Email Us</div>
    <div class="info-value">info@companyname.com</div>
    <div class="info-label">Follow Us</div>
    <div class="social">
      <span aria-label="Social profile 1"></span>
      <span aria-label="Social profile 2"></span>
      <span aria-label="Social profile 3"></span>
      <span aria-label="Social profile 4"></span>
    </div>
  </div>

  <footer class="site-footer">
    <nav class="footer-nav">
      <a href="#">Home</a><a href="#">About Us</a><a href="#">Contact Us</a><a href="#">Blog</a>
    </nav>
    <p class="copyright">© 2019 Company Name &nbsp;All right reserved</p>
  </footer>

</div>
</body>
</html>
```